Vibrant, yet professional, stationery set and other designs required.

I need to source a fantastic designer for a new project as part of my company using a new logo designed via pixel forum.

**UPDATE** I am not looking for just 'fine' design that will suffice. I am looking for something great.

We are a life assurance brokerage based in Dublin, Ireland and BrightOak.ie is our new website aimed at providing services for young families in Ireland. We are hoping to be the 'Orvo' level of service providers in this area and I am looking for the quality of design to reflect this :-) Hopefully that makes sense!

I have a preference for straight lines over curves and waves.

I need...

1. Business card
2. Letterhead
3. Banner (for printing - 76cm X 305cm)
4. Car branding for ZENTA 300 (2014 sport model) I believe the templates are freely available online.

Target Market(s)

Parents in Ireland - Aged 27 to 50.

Industry/Entity Type

Financial Planning

Colors

Designer to choose colors to be used in the design.

Requirements
Must have
• All of the items listed in the description above. I like clean, bright, legible, vibrant and professional design.
Should not have
• No silly or 'cheap' looking designs. This is a professional company looking to provide a professional service.

```html
<!DOCTYPE html>
<html lang="en">
<head>
<meta charset="utf-8">
<title>BrightOak.ie Business Card</title>
<link href="https://fonts.googleapis.com/css2?family=Open+Sans:wght@400;600;700&display=swap" rel="stylesheet">
<style>
  :root {
    --bg: #1a1a1a;
    --lime: #a2c94f;
    --lime-deep: #7ea335;
    --leaf: #7bb62f;
    --slate: #8e999e;
    --ink: #3a3a3a;
    --rule: #8a8a8a;
    --accent: #f0862a;
    --paper: #ffffff;
  }
  * { box-sizing: border-box; margin: 0; padding: 0; }
  html, body {
    width: 1200px; height: 1200px; overflow: hidden;
    background: var(--bg);
    font-family: "Open Sans", Arial, sans-serif;
  }
  .stage {
    width: 1200px; height: 1200px;
    display: flex; flex-direction: column; align-items: center; justify-content: center;
    gap: 60px;
  }
  .card {
    width: 840px; height: 480px;
    position: relative;
    box-shadow: 0 12px 30px rgba(0,0,0,.5);
  }
  .card--front {
    background: var(--lime);
    display: flex; align-items: center; justify-content: center;
  }
  .card--front .brand-name {
    color: var(--lime-deep);
    font-size: 84px; font-weight: 700;
    letter-spacing: -1px;
  }
  .card--back {
    background: var(--paper);
    display: flex; align-items: center;
  }
  .brand-block {
    width: 420px;
    display: flex; align-items: center; justify-content: center;
    padding-top: 60px;
  }
  .brand-block .brand-name {
    color: var(--slate);
    font-size: 58px; font-weight: 700;
    letter-spacing: -1px;
  }
  .divider {
    width: 2px; height: 190px;
    background: var(--rule);
    margin-top: 40px;
  }
  .contact {
    padding-left: 36px;
    margin-top: -20px;
    color: var(--ink);
    font-size: 17px; line-height: 1.3;
  }
  .contact__name {
    color: var(--leaf);
    font-size: 27px; font-weight: 700;
    line-height: 1.1;
  }
  .contact__role {
    color: var(--slate);
    font-size: 17px;
    margin-bottom: 26px;
  }
  .contact__address { margin-bottom: 18px; }
  .contact__list { list-style: none; }
  .contact__list li {
    display: flex; align-items: center; gap: 10px;
  }
  .contact__list svg { width: 14px; height: 14px; flex: none; }
</style>
</head>
<body>
<main class="stage">
  <section class="card card--front" aria-label="Card front">
    <span class="brand-name">BrightOak.ie</span>
  </section>

  <section class="card card--back" aria-label="Card back">
    <div class="brand-block">
      <span class="brand-name">BrightOak.ie</span>
    </div>
    <div class="divider"></div>
    <div class="contact">
      <p class="contact__name">Daniel Rowe</p>
      <p class="contact__role">General Manager</p>
      <p class="contact__address">55 demo street, demo place<br>P.O. Box 000, 555 Avenue</p>
      <ul class="contact__list">
        <li>
          <svg viewBox="0 0 14 14" aria-hidden="true"><path d="M3 1 L5 1 L6 4 L4.5 5 Q5.5 8 9 9.5 L10 8 L13 9 L13 11 Q12 13 10 13 Q2 11 1 3 Q1 1 3 1 Z" fill="var(--accent)"/></svg>
          888-8888-8888
        </li>
        <li>
          <svg viewBox="0 0 14 14" aria-hidden="true"><rect x="4" y="1" width="6" height="4" fill="none" stroke="var(--accent)" stroke-width="1.4"/><rect x="1" y="5" width="12" height="5" rx="1" fill="var(--accent)"/><rect x="4" y="9" width="6" height="4" fill="#fff" stroke="var(--accent)" stroke-width="1.4"/></svg>
          000-0000-0000
        </li>
        <li>
          <svg viewBox="0 0 14 14" aria-hidden="true"><rect x="1" y="3" width="12" height="8" fill="var(--accent)"/><path d="M1 3 L7 8 L13 3" fill="none" stroke="#fff" stroke-width="1.2"/></svg>
          info@websitename.com
        </li>
        <li>
          <svg viewBox="0 0 14 14" aria-hidden="true"><circle cx="7" cy="7" r="5.5" fill="none" stroke="var(--accent)" stroke-width="1.3"/><ellipse cx="7" cy="7" rx="2.3" ry="5.5" fill="none" stroke="var(--accent)" stroke-width="1.1"/><path d="M1.5 7 H12.5" stroke="var(--accent)" stroke-width="1.1"/></svg>
          www.websitename.com
        </li>
      </ul>
    </div>
  </section>
</main>
</body>
</html>
```